Kid's Cancer Camp Business Card

Create a unique Two-Sided color business cards for Camp Maple Hollow, a pediatric cancer camp.

The camp tag line is: Where brave kids get to just be kids...

Derek Talbrook, Executive Director
Camp Maple Hollow Charitable Foundation, Inc
PO Box 318
Alder Brook, VT 06917

Phone - 203-555-0142
Fax - 203-555-0187
Email: derek@campmaplehollow.org
www.campmaplehollow.org

Target Market(s)

Potential Donors, Volunteers and Campers

Industry/Entity Type

Non-profit pediatric cancer camp

Contact Information for Business Card

All contact info that is included in the description

Font styles to use
Other font styles liked:
• Designer chooses font

Requirements
Must have
• Camp Maple Hollow Logo and Tag Line
Nice to have
• should be eye catching
Should not have
• not cartoony

```html
<!DOCTYPE html>
<html lang="en">
<head>
<meta charset="utf-8">
<title>Camp Maple Hollow – Business Card</title>
<link rel="stylesheet" href="https://fonts.googleapis.com/css2?family=Open+Sans:wght@400;600;700&display=swap">
<style>
  :root {
    --backdrop: #4b4b4b;
    --card: #1a1a1a;
    --card-emboss: #232323;
    --teal: #00a19a;
    --blue: #1f62ad;
    --sun: #fbb41f;
    --white: #ffffff;
  }
  * { margin: 0; padding: 0; box-sizing: border-box; }
  html, body { width: 1200px; height: 800px; overflow: hidden; }
  body {
    background: var(--backdrop);
    font-family: "Open Sans", Arial, sans-serif;
    position: relative;
  }

  .card {
    position: absolute;
    background: var(--card);
    border-radius: 26px;
    border-bottom: 4px solid var(--teal);
    overflow: hidden;
    color: var(--white);
  }

  /* Front */
  .card-front {
    left: 110px; top: 100px;
    width: 360px; height: 600px;
  }
  .brand {
    position: absolute;
    left: 0; right: 0; top: 70px;
    display: flex; flex-direction: column; align-items: center; gap: 18px;
  }
  .brand-mark {
    width: 90px; height: 90px; border-radius: 50%;
    background: var(--sun);
  }
  .brand-name {
    font-size: 30px; font-weight: 600; color: var(--blue);
    letter-spacing: 0.5px; white-space: nowrap;
  }
  .person {
    position: absolute; left: 0; right: 0; top: 250px; text-align: center;
  }
  .person-name { font-size: 28px; font-weight: 700; color: var(--teal); }
  .person-title { font-size: 15px; margin-top: 2px; }

  .dot-row { position: absolute; left: 20px; width: 320px; height: 40px; }
  .dot-row.contact-row { top: 318px; }
  .dot-row.address-row { top: 470px; }

  .contact-list {
    position: absolute; left: 0; right: 0; top: 368px;
    text-align: center; list-style: none;
    font-size: 15px; line-height: 22px;
  }
  .address {
    position: absolute; left: 0; right: 0; top: 518px;
    text-align: center; font-style: normal;
    font-size: 14px; line-height: 20px;
  }

  /* Back */
  .card-back {
    left: 560px; top: 230px;
    width: 560px; height: 340px;
  }
  .watermark {
    position: absolute; left: 0; right: 0; top: 60px;
    display: flex; flex-direction: column; align-items: center; gap: 12px;
  }
  .watermark-mark {
    width: 110px; height: 110px; border-radius: 50%;
    background: var(--card-emboss);
    box-shadow: inset 2px 2px 4px #0d0d0d, inset -2px -2px 4px #2a2a2a;
  }
  .watermark-name {
    font-size: 42px; font-weight: 600; color: var(--card-emboss);
    line-height: 1.2; white-space: nowrap;
    text-shadow: 1px 1px 0 #2c2c2c, -1px -1px 0 #0e0e0e;
  }
  .tagline-band {
    position: absolute; left: 0; right: 0; bottom: 26px; height: 46px;
    background: var(--teal);
    display: flex; align-items: center; justify-content: center;
    font-size: 19px; font-weight: 600; letter-spacing: 0.3px;
  }
</style>
</head>
<body>

<section class="card card-front" aria-label="Business card front">
  <div class="brand">
    <span class="brand-mark"></span>
    <span class="brand-name">Camp Maple Hollow</span>
  </div>

  <div class="person">
    <div class="person-name">Derek Talbrook</div>
    <div class="person-title">Executive Director</div>
  </div>

  <svg class="dot-row contact-row" viewBox="0 0 320 40" aria-hidden="true">
    <g fill="var(--teal)">
      <circle cx="6" cy="20" r="2.5"/><circle cx="18" cy="20" r="3.5"/>
      <circle cx="32" cy="20" r="4.5"/><circle cx="48" cy="20" r="5.5"/>
      <circle cx="66" cy="20" r="6.5"/>
      <circle cx="97" cy="20" r="15"/><circle cx="139" cy="20" r="15"/>
      <circle cx="181" cy="20" r="15"/><circle cx="223" cy="20" r="15"/>
      <circle cx="254" cy="20" r="6.5"/><circle cx="272" cy="20" r="5.5"/>
      <circle cx="288" cy="20" r="4.5"/><circle cx="302" cy="20" r="3.5"/>
      <circle cx="314" cy="20" r="2.5"/>
    </g>
    <g fill="var(--white)">
      <path d="M91 12 q-3 2 -1 8 q3 7 8 8 q3 0 4 -2 l-3 -3 q-2 1 -3 0 q-2 -2 -3 -5 q0 -1 1 -2 z"/>
      <rect x="133" y="12" width="12" height="5"/>
      <rect x="131" y="18" width="16" height="9" rx="1"/>
      <path d="M173 14 h16 v12 h-16 z M173 14 l8 7 l8 -7" fill="none" stroke="var(--white)" stroke-width="2"/>
      <circle cx="223" cy="20" r="8" fill="none" stroke="var(--white)" stroke-width="2"/>
      <path d="M215 20 h16 M223 12 q-5 8 0 16 q5 -8 0 -16" fill="none" stroke="var(--white)" stroke-width="1.5"/>
    </g>
  </svg>

  <ul class="contact-list">
    <li>203-555-0142</li>
    <li>203-555-0187</li>
    <li>derek@campmaplehollow.org</li>
    <li>www.campmaplehollow.org</li>
  </ul>

  <svg class="dot-row address-row" viewBox="0 0 320 40" aria-hidden="true">
    <g fill="var(--teal)">
      <circle cx="8" cy="20" r="2.5"/><circle cx="22" cy="20" r="3.5"/>
      <circle cx="38" cy="20" r="4.5"/><circle cx="56" cy="20" r="5.5"/>
      <circle cx="76" cy="20" r="6.5"/><circle cx="98" cy="20" r="7.5"/>
      <circle cx="124" cy="20" r="9"/>
      <circle cx="160" cy="20" r="16"/>
      <circle cx="196" cy="20" r="9"/><circle cx="222" cy="20" r="7.5"/>
      <circle cx="244" cy="20" r="6.5"/><circle cx="264" cy="20" r="5.5"/>
      <circle cx="282" cy="20" r="4.5"/><circle cx="298" cy="20" r="3.5"/>
      <circle cx="312" cy="20" r="2.5"/>
    </g>
    <path d="M160 30 l-6 -9 a7 7 0 1 1 12 0 z" fill="var(--white)"/>
    <circle cx="160" cy="17" r="2.5" fill="var(--teal)"/>
  </svg>

  <address class="address">
    Camp Maple Hollow Charitable<br>
    Foundation, Inc PO Box 318<br>
    Alder Brook, VT 06917
  </address>
</section>

<section class="card card-back" aria-label="Business card back">
  <div class="watermark">
    <span class="watermark-mark"></span>
    <span class="watermark-name">Camp Maple Hollow</span>
  </div>
  <div class="tagline-band">Where brave kids get to just be kids...</div>
</section>

</body>
</html>
```